Water Delivery Service Website

We are working with BrivoNeté. They are a water delivery company and in need of a new website design.
Some sites to use for inspiration:
https://www.corvindale.example/home
https://www.plumtidego.example/en/home3
https://www.zelkop.example
https://www.hestrova.example
Thank you for taking the time to consider designing a website for us. We are web developers based in Stockton, CA, USA. Most of our projects go through the same process. Understanding this process may help you win a project with us. We custom-code all of our websites in-house. We don’t have any requirements as to what tools you use for your design, but we prefer Figma files. For any design that we label as four-stars, we send it to the client for review. The client picks the final design they want us to use. Once we complete this process, we will continue to show additional clients all the four-star sites and purchase them later. Your designs will have multiple chances to sell. For better chances of success, we ask that you follow these guidelines.
IMAGES:
If you use any images or icons in the design, we ask that you have a link to the asset so we can purchase the image/icon. Most of the designs we submit do not have the customer’s images on them unless they have some great images. Be creative; show us the feeling you are trying to portray with your image choices. Use any royalty-free site you choose. We subscribe to Quenlix and mainly use their images, but we can purchase images outside of Quenlix.
PLEASE NOTE: we will not submit designs to clients with watermarks on the images.
FONTS:
We ask that you identify the fonts used in the design. This can be done in a message if you want. We typically use Google Fonts and Quenlix Fonts.
CONTENT:
We're always open to different content and ideas. We often submit designs with stock images so the client can see our vision. We typically take pictures after the website launch to use their images with our vision. Lorem Ipsum is fine for paragraphs, but we ask that you write the headers in correct English. We want to be able to show the vision and identify the sections of the website.
INSPIRATION:
We typically add a couple of links in the brief of websites we like to help you get started in your design.
REVISIONS:
We do not often ask for revisions of the designs unless we see something in the design that may not appeal to the client. If there are slight changes that we want to make, we do that in the development process.
FEEDBACK:
We rarely give feedback on designs during the design process. We are working on many website projects and do not have the time to provide feedback. We usually respond if your request is well thought out and asks specific questions, but a note asking “feedback, please” usually goes unanswered.

```html
<!DOCTYPE html>
<html lang="en">
<head>
<meta charset="utf-8">
<title>BrivoNeté — Water Delivery</title>
<link href="https://fonts.googleapis.com/css2?family=Poppins:wght@400;500;600;700&display=swap" rel="stylesheet">
<style>
:root{
  --blue:#1c9ad9;
  --blue-dark:#1584c4;
  --navy:#1b1a57;
  --ink:#1f1d4f;
  --text:#3a3a4a;
  --light:#eaf6fc;
  --white:#ffffff;
}
*{box-sizing:border-box;margin:0;padding:0}
html,body{width:1200px;height:4743px;overflow:hidden}
body{position:relative;font-family:'Poppins',sans-serif;color:var(--text);background:var(--white)}
.abs{position:absolute}
a{color:inherit;text-decoration:none}

.topbar{left:0;top:0;width:1200px;height:52px;background:var(--blue)}
.social-dot{width:32px;height:32px;border-radius:50%;background:var(--white);top:10px;display:flex;align-items:center;justify-content:center}
.social-dot.dark{background:var(--navy)}
.social-dot span{width:10px;height:10px;border-radius:50%;background:var(--navy)}
.social-dot.dark span{background:var(--white)}
.search{left:567px;top:7px;width:257px;height:37px;border:1.5px solid rgba(255,255,255,.8);border-radius:20px;color:#fff;font-size:14px;display:flex;align-items:center;padding-left:12px;gap:10px}
.search i{width:22px;height:22px;border-radius:50%;background:var(--blue-dark);display:flex;align-items:center;justify-content:center}
.toplinks{left:856px;top:15px;color:#fff;font-size:14px;display:flex;gap:22px;align-items:center}

.header{left:0;top:52px;width:1200px;height:108px;background:#fff;box-shadow:0 2px 8px rgba(0,0,0,.06)}
.brand{display:flex;align-items:center;gap:10px}
.brand .mark{width:30px;height:30px;border-radius:50%;background:var(--blue)}
.brand .name{font-weight:500;font-size:36px;color:var(--blue);letter-spacing:.5px}
.nav{left:438px;top:94px;display:flex;gap:28px;font-size:14.5px;font-weight:500;color:var(--ink)}
.nav .on{color:var(--blue);border-bottom:2px solid var(--blue);padding-bottom:2px}
.call-ring{left:862px;top:76px;width:62px;height:62px;border-radius:50%;background:#fff;box-shadow:0 3px 12px rgba(0,0,0,.12);display:flex;align-items:center;justify-content:center}
.call-text{left:940px;top:84px;font-size:11px;font-weight:600;color:var(--ink)}
.call-text b{display:block;font-size:17px;font-weight:500;color:#777;margin-top:2px}

.hero-photo{left:0;top:160px;width:1200px;height:640px;background:linear-gradient(100deg,#8fb7d8 0%,#cfdfeb 24%,#ecebe8 45%,#d9d6d1 70%,#c9c6c0 100%)}
.hero-circle{left:598px;top:206px;width:490px;height:490px;border-radius:50%;background:#fff;box-shadow:0 6px 30px rgba(0,0,0,.12);text-align:center;padding-top:118px}
.hero-circle h1{font-weight:500;font-size:34px;line-height:43px;color:var(--ink);text-transform:uppercase}
.hero-circle p{font-size:16px;line-height:25px;color:#333;width:430px;margin:18px auto 0}
.btn{display:inline-block;background:var(--blue);color:#fff;font-size:13px;font-weight:600;text-transform:uppercase;border-radius:26px}
.hero-circle .btn{margin-top:24px;padding:15px 26px}
.dots .d{position:absolute;left:1138px;width:14px;height:14px;border-radius:50%;border:2px solid var(--navy)}
.dots .d.on{background:var(--blue);border-color:var(--blue)}
.hero-badge{left:550px;top:668px;width:100px;height:100px;border-radius:50%;background:#fff;box-shadow:0 4px 14px rgba(0,0,0,.15);display:flex;align-items:center;justify-content:center}
.hero-badge span{width:34px;height:34px;border-radius:50%;background:var(--blue)}

.title{left:0;width:1200px;text-align:center;font-weight:600;color:var(--ink);text-transform:uppercase}
.intro-title{top:860px;font-size:50px;line-height:60px}
.intro-copy{left:120px;top:1014px;width:960px;text-align:center;font-size:17px;line-height:28px;color:#333}
.svc{width:302px;height:304px;top:1126px;background:#fff;border-radius:22px;box-shadow:0 6px 18px rgba(28,154,217,.2);padding:8px}
.svc .ph{height:224px;border-radius:16px}
.svc .lbl{margin-top:28px;text-align:center;font-size:20px;font-weight:500;color:var(--blue)}

.feat-bg{left:0;top:1500px;width:1200px;height:655px}
.sec-title-w{color:#fff}
.underline{height:4px;width:72px;left:564px;border-radius:2px}
.prod{width:224px;height:284px;background:#fff;border-radius:14px;text-align:center;padding-top:30px}
.prod .bottle{width:58px;height:160px;margin:0 auto;border-radius:18px 18px 10px 10px;background:linear-gradient(90deg,#a9cde6,#e8f3fa 50%,#a3c8e2)}
.prod h4{margin-top:20px;font-size:16px;font-weight:500;color:#222}
.prod .price{margin-top:6px;font-size:15px;color:#444}
.prod .cart{position:absolute;right:14px;top:14px;width:30px;height:30px;border-radius:50%;border:1.5px solid #b9dff2;display:flex;align-items:center;justify-content:center}
.prod.hl{border:3px solid var(--blue)}
.prod.hl .cart{background:var(--blue);border-color:var(--blue)}
.prod.hl h4{text-decoration:underline}
.shadowed{box-shadow:0 6px 18px rgba(28,154,217,.22)}

.spring-title{left:110px;top:2276px;font-size:40px;line-height:52px;font-weight:600;color:var(--ink)}
.spring-copy{left:110px;top:2416px;width:488px;font-size:16.5px;line-height:27.5px;color:#333;text-align:justify}
.spring-copy p+p{margin-top:10px}
.spring-btn{left:112px;top:2670px;padding:15px 31px}
.spring-back{left:685px;top:2279px;width:429px;height:426px;background:var(--light);border-radius:26px}
.spring-photo{left:659px;top:2304px;width:431px;height:427px;border-radius:26px;background:linear-gradient(180deg,#a7bfd6 0%,#6f8ea6 45%,#48606d 72%,#37424a 100%)}

.order-bg{left:0;top:2830px;width:1200px;height:855px}
.order-ring{left:111px;top:3111px;width:452px;height:452px;border-radius:50%;background:#fff;padding:20px}
.order-ring div{width:100%;height:100%;border-radius:50%;background:linear-gradient(160deg,#e3e7e6,#b9c3c3 55%,#8fa6a4)}
.step-ic{left:599px;width:80px;height:80px;border-radius:50%;background:#fff;display:flex;align-items:center;justify-content:center}
.step{left:709px;width:380px;color:#fff}
.step h3{font-size:19px;font-weight:500;text-transform:uppercase}
.step p{font-size:13.5px;line-height:24px;margin-top:6px;text-align:justify;opacity:.95}

.foot-bg{left:0;top:4270px;width:1200px;height:473px}
.foot-h{font-size:16px;font-weight:600;color:#fff;text-transform:uppercase}
.foot-list{list-style:none;color:#fff;font-size:14px}
.foot-list li{height:41px;display:flex;align-items:flex-start;gap:18px}
.foot-list li i{width:13px;height:13px;border-radius:50%;background:var(--blue);margin-top:4px;position:relative}
.foot-list li i:after{content:"";position:absolute;left:4px;top:3.5px;border-left:5px solid #fff;border-top:3px solid transparent;border-bottom:3px solid transparent}
.contact{left:788px;color:#fff;font-size:14px;line-height:20px;display:flex;gap:20px;align-items:flex-start}
.contact i{width:34px;height:34px;border-radius:50%;background:#fff;display:flex;align-items:center;justify-content:center;flex:none}
.foot-rule{left:110px;top:4675px;width:980px;height:1px;background:rgba(255,255,255,.25)}
.copy{left:0;top:4694px;width:1200px;text-align:center;color:#fff;font-size:13.5px}
.pay{top:4698px;width:33px;height:20px;border-radius:3px}
</style>
</head>
<body>

<div class="abs topbar"></div>
<div class="abs social-dot dark" style="left:111px" aria-label="Social network"><span></span></div>
<div class="abs social-dot" style="left:155px" aria-label="Social network"><span></span></div>
<div class="abs social-dot" style="left:197px" aria-label="Social network"><span></span></div>
<div class="abs search"><i><svg width="11" height="11" viewBox="0 0 12 12"><circle cx="5" cy="5" r="3.8" fill="none" stroke="#fff" stroke-width="1.6"/><path d="M8 8l3 3" stroke="#fff" stroke-width="1.6"/></svg></i>Search</div>
<div class="abs toplinks">
  <span style="display:flex;align-items:center;gap:6px"><svg width="15" height="15" viewBox="0 0 16 16"><circle cx="8" cy="8" r="7" fill="none" stroke="#fff" stroke-width="1.4"/><circle cx="8" cy="6.5" r="2.4" fill="#fff"/><path d="M3.6 12.8c1-2 2.6-2.8 4.4-2.8s3.4.8 4.4 2.8" fill="#fff"/></svg>My Account</span>
  <span>|</span>
  <span style="display:flex;align-items:center;gap:6px">Cart <svg width="15" height="13" viewBox="0 0 16 14"><path d="M0 1h3l2 8h8l2-6H4" fill="none" stroke="#fff" stroke-width="1.5"/><circle cx="6" cy="12" r="1.4" fill="#fff"/><circle cx="12" cy="12" r="1.4" fill="#fff"/></svg>(0)</span>
</div>

<div class="abs header"></div>
<div class="abs brand" style="left:110px;top:84px"><span class="mark"></span><span class="name">BrivoNeté</span></div>
<nav class="abs nav"><a class="on">Home</a><a>Water Your Way</a><a>Shop</a><a>Learn</a><a>About</a></nav>
<div class="abs call-ring"><svg width="26" height="26" viewBox="0 0 24 24"><path d="M6.6 3.5l2.6 3.4-1.6 2.2c1.2 2.6 3.3 4.7 5.9 5.9l2.2-1.6 3.4 2.6-1.3 3.3C11 19.6 4.4 13 3.3 4.8z" fill="none" stroke="#1c9ad9" stroke-width="1.4" stroke-linejoin="round"/></svg></div>
<div class="abs call-text">Call Us:<b>+1 (555) 014 2290</b></div>

<div class="abs hero-photo" role="img" aria-label="Bright kitchen with a large blue water delivery bottle in the foreground"></div>
<svg class="abs" style="left:0;top:700px" width="1200" height="100" viewBox="0 0 1200 100" aria-hidden="true"><path d="M0 100V92C120 92 200 40 300 40S430 70 520 60 640 12 760 30 880 66 960 48 1100 30 1200 22V100Z" fill="#fff"/></svg>
<div class="abs hero-circle">
  <h1>Reliable water<br>delivery, when you<br>need it most.</h1>
  <p>Lorem ipsum dolor sit amet, consectetur adipiscing elit, sed do eiusmod tempor incididunt ut labore magna eiusmod tempor aliqua.</p>
  <a class="btn">Start Water Delivery</a>
</div>
<div class="dots"><span class="d" style="top:416px"></span><span class="d on" style="top:440px"></span><span class="d" style="top:462px"></span><span class="d" style="top:486px"></span></div>
<div class="abs hero-badge"><span></span></div>

<h2 class="abs title intro-title">Our whole world<br>is water</h2>
<p class="abs intro-copy">Lorem ipsum dolor sit amet, consectetur adipiscing elit, sed do eiusmod tempor incididunt ut labore et dolore magna aliqua. Ut enim ad minim veniam, quis nostrud exercitation ullamco laboris nisi ut aliquip ex ea commodo duis aute irure dolor in ad minim veniam reprehenderit.</p>

<div class="abs svc" style="left:112px"><div class="ph" role="img" aria-label="Delivery worker carrying a water bottle to a home doorway" style="background:linear-gradient(120deg,#3f5d74,#6f9a58 45%,#c9c4b6)"></div><div class="lbl">Home Delivery <svg width="18" height="10" viewBox="0 0 18 10"><path d="M0 5h15M11 1l4 4-4 4" fill="none" stroke="#1c9ad9" stroke-width="2"/></svg></div></div>
<div class="abs svc" style="left:449px"><div class="ph" role="img" aria-label="Two delivery workers carrying water bottles beside a van" style="background:linear-gradient(120deg,#c9ced4,#5b8fc7 50%,#d7dadd)"></div><div class="lbl">Office Delivery <svg width="18" height="10" viewBox="0 0 18 10"><path d="M0 5h15M11 1l4 4-4 4" fill="none" stroke="#1c9ad9" stroke-width="2"/></svg></div></div>
<div class="abs svc" style="left:786px"><div class="ph" role="img" aria-label="Worker loading many water bottles into a van" style="background:linear-gradient(120deg,#2c3440,#3d6fb0 50%,#7d8a96)"></div><div class="lbl">Bulk Orders <svg width="18" height="10" viewBox="0 0 18 10"><path d="M0 5h15M11 1l4 4-4 4" fill="none" stroke="#1c9ad9" stroke-width="2"/></svg></div></div>

<svg class="abs feat-bg" viewBox="0 0 1200 655" aria-hidden="true"><path d="M0 360C300-80 900-80 1200 250V655H0Z" fill="#1c9ad9"/><path d="M0 420C300-30 900-30 1200 300V655H0Z" fill="#1b1a57"/></svg>
<h2 class="abs title sec-title-w" style="top:1670px;font-size:48px">Featured Products</h2>
<div class="abs underline" style="top:1732px;background:#fff"></div>
<svg class="abs" style="left:38px;top:1914px" width="40" height="26" viewBox="0 0 40 26"><path d="M38 13H3M14 2L3 13l11 11" fill="none" stroke="#fff" stroke-width="2.2"/></svg>
<svg class="abs" style="left:1122px;top:1914px" width="40" height="26" viewBox="0 0 40 26"><path d="M2 13h35M26 2l11 11-11 11" fill="none" stroke="#fff" stroke-width="2.2"/></svg>

<div class="abs prod" style="left:112px;top:1785px"><span class="cart"><svg width="13" height="12" viewBox="0 0 16 14"><path d="M0 1h3l2 8h8l2-6H4z" fill="#1c9ad9"/><circle cx="6" cy="12" r="1.4" fill="#1c9ad9"/><circle cx="12" cy="12" r="1.4" fill="#1c9ad9"/></svg></span><div class="bottle" role="img" aria-label="500ml water bottle"></div><h4>500ml Spring Bottle</h4><div class="price">$29.00</div></div>
<div class="abs prod" style="left:363px;top:1785px"><span class="cart"><svg width="13" height="12" viewBox="0 0 16 14"><path d="M0 1h3l2 8h8l2-6H4z" fill="#1c9ad9"/><circle cx="6" cy="12" r="1.4" fill="#1c9ad9"/><circle cx="12" cy="12" r="1.4" fill="#1c9ad9"/></svg></span><div class="bottle" role="img" aria-label="500ml water bottle"></div><h4>500ml Spring Bottle</h4><div class="price">$29.00</div></div>
<div class="abs prod hl" style="left:611px;top:1783px;width:228px;height:288px"><span class="cart"><svg width="13" height="12" viewBox="0 0 16 14"><path d="M0 1h3l2 8h8l2-6H4z" fill="#fff"/><circle cx="6" cy="12" r="1.4" fill="#fff"/><circle cx="12" cy="12" r="1.4" fill="#fff"/></svg></span><div class="bottle" role="img" aria-label="500ml water bottle"></div><h4>500ml Spring Bottle</h4><div class="price">$29.00</div></div>
<div class="abs prod" style="left:865px;top:1785px"><span class="cart"><svg width="13" height="12" viewBox="0 0 16 14"><path d="M0 1h3l2 8h8l2-6H4z" fill="#1c9ad9"/><circle cx="6" cy="12" r="1.4" fill="#1c9ad9"/><circle cx="12" cy="12" r="1.4" fill="#1c9ad9"/></svg></span><div class="bottle" role="img" aria-label="500ml water bottle"></div><h4>500ml Spring Bottle</h4><div class="price">$29.00</div></div>

<h2 class="abs spring-title">100% MOUNTAIN<br>SPRING WATER</h2>
<div class="abs underline" style="left:110px;top:2381px;background:var(--blue)"></div>
<div class="abs spring-copy">
  <p>Lorem ipsum dolor sit amet, consectetur adipiscing elit, sed do eiusmod tempor incididunt ut labore et dolore magna aliqua. Ut enim ad minim veniam, quis nostrud exercitation ullamco laboris nisi ut aliquip ex ea commodo consequat duis aute irurea.</p>
  <p>Lorem ipsum dolor sit amet, consectetur adipiscing elit, sed do eiusmod tempor incididunt ut labore et dolore magna aliqua.</p>
</div>
<a class="abs btn spring-btn">Explore Our Products</a>
<div class="abs spring-back"></div>
<div class="abs spring-photo" role="img" aria-label="Large water bottle standing in a mountain stream"></div>

<svg class="abs order-bg" viewBox="0 0 1200 855" aria-hidden="true"><path d="M0 30C60 30 90 10 150 22S240 60 320 50 400 0 480 8 560 50 640 44 720 6 800 10 880 48 960 46 1040 8 1120 10 1170 30 1200 34V855H0Z" fill="#1c9ad9"/></svg>
<h2 class="abs title sec-title-w" style="top:2980px;font-size:52px;font-weight:500">Order Process</h2>
<div class="abs underline" style="top:3051px;background:#fff"></div>
<div class="abs order-ring"><div role="img" aria-label="Woman drinking from a water bottle outdoors"></div></div>

<div class="abs step-ic" style="top:3113px"><svg width="42" height="42" viewBox="0 0 42 42"><path d="M34 14A15 15 0 1 0 36 21" fill="none" stroke="#1b1a57" stroke-width="3"/><path d="M36 8v7h-7" fill="none" stroke="#1b1a57" stroke-width="3"/><path d="M21 11v10h7" fill="none" stroke="#1b1a57" stroke-width="3"/></svg></div>
<div class="abs step-ic" style="top:3238px"><svg width="42" height="42" viewBox="0 0 42 42"><circle cx="21" cy="21" r="11" fill="none" stroke="#1b1a57" stroke-width="6" stroke-dasharray="5 3.6"/><circle cx="21" cy="21" r="8" fill="none" stroke="#1b1a57" stroke-width="3"/><circle cx="21" cy="21" r="3" fill="#1b1a57"/></svg></div>
<div class="abs step-ic" style="top:3363px"><svg width="42" height="42" viewBox="0 0 42 42"><circle cx="21" cy="21" r="15" fill="none" stroke="#1b1a57" stroke-width="2.5"/><path d="M21 11c4 6 7 9 7 13a7 7 0 0 1-14 0c0-4 3-7 7-13z" fill="#1b1a57"/></svg></div>
<div class="abs step-ic" style="top:3486px"><svg width="42" height="42" viewBox="0 0 42 42"><circle cx="21" cy="21" r="16" fill="#1b1a57"/><circle cx="21" cy="21" r="11" fill="none" stroke="#fff" stroke-width="2"/><path d="M15 21l4 4 8-8" fill="none" stroke="#fff" stroke-width="3"/></svg></div>

<div class="abs step" style="top:3098px"><h3>Delivery Service</h3><p>Lorem ipsum dolor sit amet, consectetur adipiscing elit, sed do eiusmod tempor incididunt ut labore et dolore magna aliqua. Ut enim adea.</p></div>
<div class="abs step" style="top:3223px"><h3>Custom &amp; Label</h3><p>Lorem ipsum dolor sit amet, consectetur adipiscing elit, sed do eiusmod tempor incididunt ut labore et dolore magna aliqua. Ut enim adea.</p></div>
<div class="abs step" style="top:3348px"><h3>Products &amp; Solutions</h3><p>Lorem ipsum dolor sit amet, consectetur adipiscing elit, sed do eiusmod tempor incididunt ut labore et dolore magna aliqua. Ut enim adea.</p></div>
<div class="abs step" style="top:3471px"><h3>Best Quality</h3><p>Lorem ipsum dolor sit amet, consectetur adipiscing elit, sed do eiusmod tempor incididunt ut labore et dolore magna aliqua. Ut enim adea.</p></div>

<h2 class="abs title" style="top:3789px;font-size:48px">Best Sellers</h2>
<div class="abs underline" style="top:3851px;background:var(--blue)"></div>
<svg class="abs" style="left:38px;top:4033px" width="40" height="26" viewBox="0 0 40 26"><path d="M38 13H3M14 2L3 13l11 11" fill="none" stroke="#1b1a57" stroke-width="2.2"/></svg>
<svg class="abs" style="left:1122px;top:4033px" width="40" height="26" viewBox="0 0 40 26"><path d="M2 13h35M26 2l11 11-11 11" fill="none" stroke="#1b1a57" stroke-width="2.2"/></svg>

<div class="abs prod shadowed" style="left:112px;top:3904px"><span class="cart"><svg width="13" height="12" viewBox="0 0 16 14"><path d="M0 1h3l2 8h8l2-6H4z" fill="#1c9ad9"/><circle cx="6" cy="12" r="1.4" fill="#1c9ad9"/><circle cx="12" cy="12" r="1.4" fill="#1c9ad9"/></svg></span><div class="bottle" role="img" aria-label="500ml water bottle"></div><h4>500ml Spring Bottle</h4><div class="price">$29.00</div></div>
<div class="abs prod shadowed" style="left:363px;top:3904px"><span class="cart"><svg width="13" height="12" viewBox="0 0 16 14"><path d="M0 1h3l2 8h8l2-6H4z" fill="#1c9ad9"/><circle cx="6" cy="12" r="1.4" fill="#1c9ad9"/><circle cx="12" cy="12" r="1.4" fill="#1c9ad9"/></svg></span><div class="bottle" role="img" aria-label="500ml water bottle"></div><h4>500ml Spring Bottle</h4><div class="price">$29.00</div></div>
<div class="abs prod hl shadowed" style="left:611px;top:3902px;width:228px;height:288px"><span class="cart"><svg width="13" height="12" viewBox="0 0 16 14"><path d="M0 1h3l2 8h8l2-6H4z" fill="#fff"/><circle cx="6" cy="12" r="1.4" fill="#fff"/><circle cx="12" cy="12" r="1.4" fill="#fff"/></svg></span><div class="bottle" role="img" aria-label="500ml water bottle"></div><h4>500ml Spring Bottle</h4><div class="price">$29.00</div></div>
<div class="abs prod shadowed" style="left:865px;top:3904px"><span class="cart"><svg width="13" height="12" viewBox="0 0 16 14"><path d="M0 1h3l2 8h8l2-6H4z" fill="#1c9ad9"/><circle cx="6" cy="12" r="1.4" fill="#1c9ad9"/><circle cx="12" cy="12" r="1.4" fill="#1c9ad9"/></svg></span><div class="bottle" role="img" aria-label="500ml water bottle"></div><h4>500ml Spring Bottle</h4><div class="price">$29.00</div></div>

<svg class="abs foot-bg" viewBox="0 0 1200 473" aria-hidden="true"><path d="M0 150C300-30 900-30 1200 110V473H0Z" fill="#1c9ad9"/><path d="M0 200C300 10 900 10 1200 150V473H0Z" fill="#1b1a57"/></svg>
<div class="abs brand" style="left:110px;top:4516px"><span class="mark" style="background:#fff"></span><span class="name" style="color:#fff;font-size:34px">BrivoNeté</span></div>
<div class="abs social-dot" style="left:151px;top:4587px" aria-label="Social network"><span style="background:var(--blue)"></span></div>
<div class="abs social-dot" style="left:195px;top:4587px;background:var(--blue);border:2px solid #fff" aria-label="Social network"><span style="background:#fff"></span></div>
<div class="abs social-dot" style="left:239px;top:4587px" aria-label="Social network"><span style="background:var(--blue)"></span></div>

<h5 class="abs foot-h" style="left:374px;top:4427px">Quick Links</h5>
<ul class="abs foot-list" style="left:374px;top:4470px"><li><i></i>Home</li><li><i></i>Water Your Way</li><li><i></i>Shop</li><li><i></i>Learn</li><li><i></i>About</li></ul>
<h5 class="abs foot-h" style="left:569px;top:4427px">Other Links</h5>
<ul class="abs foot-list" style="left:569px;top:4470px"><li><i></i>Privacy Policy</li><li><i></i>Terms Of Use</li><li><i></i>Legal Support</li><li><i></i>Disclaimer</li></ul>
<h5 class="abs foot-h" style="left:788px;top:4427px">Contact Us</h5>
<div class="abs contact" style="top:4472px"><i><svg width="14" height="18" viewBox="0 0 14 18"><path d="M7 17S1 10 1 6.5a6 6 0 0 1 12 0C13 10 7 17 7 17z" fill="#1c9ad9"/><circle cx="7" cy="6.5" r="2.2" fill="#fff"/></svg></i><span>218 Fenwold Lane, Harrow Bay,<br>United States</span></div>
<div class="abs contact" style="top:4525px"><i><svg width="16" height="12" viewBox="0 0 16 12"><rect x="0.5" y="0.5" width="15" height="11" rx="1.5" fill="#1c9ad9"/><path d="M1 1l7 6 7-6" fill="none" stroke="#fff" stroke-width="1.3"/></svg></i><span style="margin-top:7px">info@brivonete.example</span></div>
<div class="abs contact" style="top:4575px"><i><svg width="16" height="16" viewBox="0 0 24 24"><path d="M6.6 3.5l2.6 3.4-1.6 2.2c1.2 2.6 3.3 4.7 5.9 5.9l2.2-1.6 3.4 2.6-1.3 3.3C11 19.6 4.4 13 3.3 4.8z" fill="#1c9ad9"/></svg></i><span style="margin-top:7px">+1 (555) 014 2290</span></div>

<div class="abs foot-rule"></div>
<div class="abs copy">© 2025 BrivoNeté All Rights Reserved</div>
<div class="abs pay" style="left:907px;background:#ffffff" aria-label="Payment card"></div>
<div class="abs pay" style="left:944px;background:#eef1f8" aria-label="Payment card"></div>
<div class="abs pay" style="left:981px;background:#f4f4f4" aria-label="Payment card"></div>
<div class="abs pay" style="left:1018px;background:#cfe6f8" aria-label="Payment card"></div>
<div class="abs pay" style="left:1055px;background:#f7f7f7" aria-label="Payment card"></div>

</body>
</html>
```